event catering company brochure & menus

i have a collaboration of different menus that i would like redesigning each one for expanding my company to the uae

Along with this i would like them to be formatted into a brochure to use & photos attached to what is suitable

Target Market(s)

corperate customers

Industry/Entity Type

catering

```html
<!DOCTYPE html>
<html lang="en">
<head>
<meta charset="utf-8">
<title>Vellanora – Tri-fold Menu Brochure</title>
<link rel="stylesheet" href="https://fonts.googleapis.com/css2?family=Questrial&family=Open+Sans:ital,wght@0,400;0,600;0,700;1,400&display=swap">
<style>
  :root{
    --canvas:#4a4a4a;
    --paper:#ffffff;
    --ink:#1f1f1f;
    --ink-soft:#444444;
    --panel-dark:#3a3a3a;
    --pill-dark:#2b2b2b;
    --rule:#8a8a8a;
    --photo-light:#d9d6d0;
    --photo-mid:#9c9a94;
    --photo-deep:#5d5a55;
  }
  *{box-sizing:border-box;margin:0;padding:0}
  html,body{width:800px;height:1200px;overflow:hidden}
  body{
    background:var(--canvas);
    font-family:"Open Sans",Arial,sans-serif;
    color:var(--ink);
    display:flex;align-items:center;justify-content:center;
  }
  .brochure{display:flex;gap:10px}
  .panel{width:250px;height:522px;position:relative;overflow:hidden;background:var(--paper)}

  /* photo placeholders */
  .photo{position:absolute;left:0;width:100%;
    background:linear-gradient(160deg,var(--photo-light) 0%,var(--photo-mid) 55%,var(--photo-deep) 100%)}
  .photo-curve{position:absolute;left:0;width:100%;display:block}

  /* left panel */
  .panel--menu .photo{top:0;height:205px}
  .panel--menu .photo-curve{top:150px;height:60px}
  .menu-body{position:absolute;top:212px;left:0;right:0;padding:0 14px;text-align:center}
  .pill{display:inline-block;background:var(--pill-dark);color:#fff;
    font-style:italic;font-size:12px;letter-spacing:.5px;text-transform:uppercase;
    padding:1px 20px;border-radius:10px;min-width:128px}
  .pill--light{background:#fff;color:var(--ink)}
  .intro-title{font-size:10.5px;font-weight:600;margin-top:5px}
  .intro-note{font-size:7.4px;color:var(--ink-soft);margin:2px 0 6px}
  .intro-lead{font-size:9.6px;color:var(--ink-soft);line-height:1.3;margin:5px 0 6px}
  .dish{margin-bottom:6px}
  .dish-name{display:inline-block;font-size:10.5px;font-weight:600;padding:0 4px 1px;
    border-bottom:1px dotted var(--ink)}
  .dish-desc{font-size:7.2px;color:var(--ink-soft);line-height:1.3;margin-top:2px}

  /* middle panel */
  .panel--starters{background:var(--panel-dark);color:#fff}
  .frame{position:absolute;inset:10px 7px 8px;border:1px solid #cfcfcf;border-top:none}
  .starters-pill{position:absolute;top:4px;left:50%;transform:translateX(-50%)}
  .starters-list{position:absolute;top:30px;left:16px;right:16px;text-align:center}
  .panel--starters .dish{border-bottom:1px dotted #e0e0e0;padding-bottom:3px;margin-bottom:5px}
  .panel--starters .dish-name{border:none;color:#fff;padding:0}
  .panel--starters .dish-desc{color:#e8e8e8;margin-top:1px}
  .contact{position:absolute;bottom:18px;left:16px;right:16px;text-align:center}
  .contact-title{font-style:italic;font-size:14px;letter-spacing:.5px}
  .contact-text{font-style:italic;font-size:7px;line-height:1.35;margin:3px 0 6px}
  .contact-line{display:flex;align-items:center;justify-content:center;gap:5px;font-size:7px;margin-top:3px}
  .contact-line svg{width:8px;height:8px;fill:#fff}

  /* right panel */
  .brand{position:absolute;top:38px;left:0;right:0;text-align:center;
    font-family:"Questrial",Arial,sans-serif;font-size:19px;letter-spacing:5px;color:var(--ink)}
  .headline{position:absolute;top:90px;left:0;right:0;text-align:center;
    font-family:"Questrial",Arial,sans-serif;font-weight:400;font-size:25px;line-height:1.2;color:var(--ink)}
  .tagline{position:absolute;top:162px;left:20px;right:20px;text-align:center;
    font-size:8.5px;line-height:1.4;color:var(--ink-soft)}
  .panel--cover .photo{top:218px;height:304px}
  .panel--cover .photo-curve{top:210px;height:50px}
</style>
</head>
<body>
<main class="brochure">

  <section class="panel panel--menu">
    <div class="photo" role="img" aria-label="Photo of a long banquet table set with plates, glasses and small potted herbs"></div>
    <svg class="photo-curve" viewBox="0 0 250 60" preserveAspectRatio="none" aria-hidden="true">
      <path d="M0,38 Q120,-8 250,26 L250,60 L0,60 Z" fill="#fff"/>
      <path d="M0,33 Q120,-14 250,20" fill="none" stroke="#1f1f1f" stroke-width="1.4"/>
    </svg>
    <div class="menu-body">
      <span class="pill">For the table</span>
      <p class="intro-title">Homemade organic flavoured sourdough</p>
      <p class="intro-note">Sea salt butter, Tuscan olive oil &amp; 10 year aged balsamic dip</p>
      <span class="pill">Starters</span>
      <p class="intro-lead">Please see bottom of the list for sharing table picnic starter dishes</p>
      <div class="dish"><span class="dish-name">Canadian Lobster salad</span>
        <p class="dish-desc">Dried tomato pearls, asparagus, baby potatoes with lobster mayonnaise</p></div>
      <div class="dish"><span class="dish-name">Harrowfield Duck breast salad</span>
        <p class="dish-desc">Grilled pineapple, cucumber &amp; beetroot</p></div>
      <div class="dish"><span class="dish-name">Braised beef cheek</span>
        <p class="dish-desc">Celeriac, poached raisins, apple puree &amp; roast pork jus</p></div>
      <div class="dish"><span class="dish-name">Duo of mackerel</span>
        <p class="dish-desc">Sweet cured &amp; torched with horseradish &amp; celeriac &amp; pickled beetroot</p></div>
    </div>
  </section>

  <section class="panel panel--starters">
    <div class="frame"></div>
    <span class="pill pill--light starters-pill">Starters</span>
    <div class="starters-list">
      <div class="dish"><span class="dish-name">Spiced monkfish tail</span>
        <p class="dish-desc">Pickled carrots, lentil Dahl &amp; yoghurt</p></div>
      <div class="dish"><span class="dish-name">Chermoula roasted salmon</span>
        <p class="dish-desc">Cumin &amp; coriander fried chickpeas, tzatziki &amp; charred flatbread</p></div>
      <div class="dish"><span class="dish-name">Beetroot risotto</span>
        <p class="dish-desc">Horseradish crème fraiche, whipped goat's cheese &amp; beetroot crisps with walnuts</p></div>
      <div class="dish"><span class="dish-name">Selection of traditional sashimi &amp; nigiri</span>
        <p class="dish-desc">Served with soy sauce, fresh wasabi, pickled ginger &amp; miso soup bowl</p></div>
      <div class="dish"><span class="dish-name">Barbecued Catalan style octopus</span>
        <p class="dish-desc">with caramelized white peaches, chorizo &amp; black olive tapenade</p></div>
      <div class="dish"><span class="dish-name">Baja fish tacos</span>
        <p class="dish-desc">Charred corn tortillas, Mexican corn salsa with avocado &amp; chipotle mayonnaise</p></div>
      <div class="dish"><span class="dish-name">Antipasti</span>
        <p class="dish-desc">Burrata (Puglia's special buffalo mozzarella) beef ham, marinated &amp; dried tomatoes with basil &amp; rocket</p></div>
      <div class="dish"><span class="dish-name">Shin of beef ravioli</span>
        <p class="dish-desc">Celeriac &amp; horseradish puree &amp; root vegetable duxelle</p></div>
    </div>
    <div class="contact">
      <p class="contact-title">CONTACT US</p>
      <p class="contact-text">Lorem Ipsum is simply dummy text of the printing and typesetting industry</p>
      <p class="contact-line">
        <svg viewBox="0 0 24 24" aria-hidden="true"><path d="M6.6 10.8a15.1 15.1 0 0 0 6.6 6.6l2.2-2.2a1 1 0 0 1 1-.25 11.4 11.4 0 0 0 3.6.57 1 1 0 0 1 1 1V20a1 1 0 0 1-1 1A17 17 0 0 1 3 4a1 1 0 0 1 1-1h3.5a1 1 0 0 1 1 1c0 1.250.2 2.45.57 3.57a1 1 0 0 1-.25 1z"/></svg>
        123 1234 123 / 123 0000 123</p>
      <p class="contact-line">
        <svg viewBox="0 0 24 24" aria-hidden="true"><circle cx="12" cy="12" r="10" fill="none" stroke="#fff" stroke-width="2"/><path d="M2 12h20M12 2c3 3 3 17 0 20M12 2c-3 3-3 17 0 20" fill="none" stroke="#fff" stroke-width="1.6"/></svg>
        www.vellanora-catering.com</p>
    </div>
  </section>

  <section class="panel panel--cover">
    <p class="brand">VELLANORA</p>
    <h1 class="headline">WHAT IS<br>LOREM IPSUM</h1>
    <p class="tagline">Lorem Ipsum is simply dummy text of the printing and typesetting industry</p>
    <div class="photo" role="img" aria-label="Photo of a dressed dining table with wine glasses, white plates, cutlery and salads"></div>
    <svg class="photo-curve" viewBox="0 0 250 50" preserveAspectRatio="none" aria-hidden="true">
      <path d="M0,0 L250,0 L250,22 Q125,-4 0,22 Z" fill="#fff"/>
      <path d="M0,18 Q125,-8 250,18" fill="none" stroke="#1f1f1f" stroke-width="1.4"/>
    </svg>
  </section>

</main>
</body>
</html>
```